Professional law firm looking for new professional and eye-catching business card design

Law firm in need of new business card design using existing firm logo and firm colors on thick card stock. Firm colors are navy blue, cyan blue, and gray. Please use firm's logo either on the back of the card or on the front and back. I am looking for something eye-catching and resonating but also professional.

Target Market(s)

Law firm growth by attracting clients with professional, creative, and attractive business cards.

Industry/Entity Type

Legal/Law Firm

Contact Information for Business Card

Name: Derek T. Halloway, Esq., Address: 517 E. Quintley Blvd., P.O. Box 641, Tavares, FL 32790, Phone numbers: (352) 555-0187 Office, (352) 555-0142 Fax, email address: DerekH@hqlegalfx.com, website: www.HQLegalFX.com

Font styles to use
Other font styles liked:
• Font as close as possible to matching law firm logo.

Requirements
Must have
• Must have business card details and law firm logo with law firm colors.

```html
<!DOCTYPE html>
<html lang="en">
<head>
<meta charset="utf-8">
<title>HQ Legal – Business Card</title>
<link rel="stylesheet" href="https://fonts.googleapis.com/css2?family=Fjalla+One&family=Montserrat:wght@400;500;600&display=swap">
<style>
  :root {
    --backdrop: #1d1e21;
    --card-light: #ffffff;
    --card-dark: #23272e;
    --cyan: #1da1e6;
    --gray: #9a9ca0;
    --ink: #2a2a2a;
  }
  * { margin: 0; padding: 0; box-sizing: border-box; }
  html, body { width: 1200px; height: 1200px; overflow: hidden; }
  body {
    background: var(--backdrop);
    font-family: "Montserrat", sans-serif;
    position: relative;
  }
  .card {
    position: absolute;
    top: 250px;
    width: 400px;
    height: 700px;
    border-radius: 30px;
    display: flex;
    flex-direction: column;
    align-items: center;
  }
  .card-front { left: 170px; background: var(--card-light); padding-top: 110px; }
  .card-back { left: 630px; background: var(--card-dark); justify-content: center; }

  .firm-mark {
    display: flex;
    align-items: center;
    gap: 14px;
    font-family: "Montserrat", sans-serif;
    font-weight: 600;
    font-size: 40px;
    letter-spacing: 3px;
    color: var(--cyan);
  }
  .firm-mark .dot {
    width: 16px; height: 16px; border-radius: 50%;
    background: var(--gray);
  }
  .card-back .firm-mark { font-size: 48px; }

  .attorney-name {
    margin-top: 110px;
    font-family: "Fjalla One", sans-serif;
    font-size: 30px;
    color: var(--cyan);
    letter-spacing: 0.5px;
  }
  .attorney-title {
    font-size: 17px;
    color: var(--ink);
    margin-top: 2px;
  }
  .icon-row {
    display: flex;
    align-items: center;
    gap: 8px;
    margin-top: 22px;
  }
  .icon-row .rule { width: 56px; height: 2px; background: var(--cyan); }
  .icon-row svg { width: 24px; height: 24px; display: block; }
  .contact-list {
    list-style: none;
    text-align: center;
    margin-top: 22px;
    font-size: 17px;
    line-height: 27px;
    color: var(--ink);
  }
  .contact-list .accent { color: var(--cyan); }
  .divider { width: 56px; height: 2px; background: var(--cyan); margin-top: 26px; }
  .address {
    margin-top: 26px;
    font-size: 16px;
    line-height: 25px;
    color: var(--ink);
    text-align: center;
    font-style: normal;
  }
</style>
</head>
<body>
  <section class="card card-front">
    <div class="firm-mark"><span class="dot"></span>HQ LEGAL</div>
    <h1 class="attorney-name">Derek T. Halloway, Esq.</h1>
    <p class="attorney-title">Attorney at Law</p>
    <div class="icon-row">
      <span class="rule"></span>
      <svg viewBox="0 0 24 24" aria-label="phone"><rect width="24" height="24" rx="6" fill="#1da1e6"/><path d="M8 6l2 0 1 3-1.5 1a7 7 0 0 0 4.5 4.5l1-1.5 3 1v2a2 2 0 0 1-2 2A11 11 0 0 1 6 8a2 2 0 0 1 2-2z" fill="#fff"/></svg>
      <svg viewBox="0 0 24 24" aria-label="fax"><rect width="24" height="24" rx="6" fill="#1da1e6"/><rect x="7" y="5" width="10" height="5" fill="#fff"/><rect x="5" y="10" width="14" height="7" rx="1" fill="#fff"/><rect x="8" y="14" width="8" height="5" fill="#fff" stroke="#1da1e6" stroke-width="1"/></svg>
      <svg viewBox="0 0 24 24" aria-label="email"><rect width="24" height="24" rx="6" fill="#1da1e6"/><rect x="5" y="7" width="14" height="10" rx="1" fill="#fff"/><path d="M5 8l7 5 7-5" fill="none" stroke="#1da1e6" stroke-width="1.5"/></svg>
      <svg viewBox="0 0 24 24" aria-label="website"><rect width="24" height="24" rx="6" fill="#1da1e6"/><circle cx="12" cy="12" r="6" fill="none" stroke="#fff" stroke-width="1.6"/><ellipse cx="12" cy="12" rx="2.6" ry="6" fill="none" stroke="#fff" stroke-width="1.3"/><path d="M6 12h12" stroke="#fff" stroke-width="1.3"/></svg>
      <span class="rule"></span>
    </div>
    <ul class="contact-list">
      <li>(352) 555-0187</li>
      <li>(352) 555-0142</li>
      <li>DerekH@hqlegalfx.com</li>
      <li>www.<span class="accent">HQLegalFX</span>.com</li>
    </ul>
    <span class="divider"></span>
    <address class="address">517 E. Quintley Blvd.,<br>P.O. Box 641, Tavares, FL 32790</address>
  </section>

  <section class="card card-back">
    <div class="firm-mark"><span class="dot"></span>HQ LEGAL</div>
  </section>
</body>
</html>
```